Speisekarten-Design für Gastronomiebetrieb
Zielgruppe
Wir sind ein Gastronomiebetrieb in einer Studentenstadt. Unsere Hauptzielgruppe sind junge Menschen und Studenten, aber auch älteres Puplikum. Wir möchten gerne ein neues Speisekartendesign, da unser aktuelles seit über 10 Jahren sich kaum verändert hat.
Aufgabenstellung
Gerne könne Sie sich die aktulle Speisekarte auf der unserer Hompeage anschauen: www.tomello-kassel.de
Auf der Frontseite soll die Farbrichtung Orange und natürlich das Logo beibehalten werden. Für die restlichen Seiten gibt es diese Einschränkung nicht. Uns ist wichtig, dass die Speisekarte modern, bunt und peppig ist. Das heisst möglichst mit kräftigen Farben und Bildern von Speisen und Getränken arbeiten.

```html
<!DOCTYPE html>
<html lang="de">
<head>
<meta charset="utf-8">
<title>Tomello – Speisekarte</title>
<link rel="stylesheet" href="https://fonts.googleapis.com/css2?family=Montserrat:wght@400;600;700&family=Dancing+Script:wght@600&display=swap">
<style>
  :root {
    --backdrop: #eef5f5;
    --orange: #f2a73a;
    --orange-light: #f6b94f;
    --red: #b8262f;
    --gold: #f0b23c;
    --ring: #f8c978;
    --ink: #5a3410;
  }
  * { margin: 0; padding: 0; box-sizing: border-box; }
  html, body {
    width: 963px; height: 1200px; overflow: hidden;
    background: var(--backdrop);
  }
  .menu-cover {
    position: absolute; left: 222px; top: 50px;
    width: 518px; height: 1100px;
    background: linear-gradient(160deg, var(--orange-light), var(--orange));
    font-family: "Montserrat", sans-serif;
  }
  .side-band {
    position: absolute; left: 0; top: 0; bottom: 0; width: 94px;
    background: var(--red);
    display: flex; justify-content: center; padding-top: 150px;
  }
  .side-band__tagline {
    writing-mode: vertical-rl;
    font-family: "Dancing Script", cursive;
    font-size: 30px; color: var(--gold); letter-spacing: 2px;
  }
  .brand {
    position: absolute; right: 28px; top: 30px; text-align: right;
  }
  .brand__name {
    font-weight: 700; font-size: 66px; color: var(--red);
    letter-spacing: 2px; line-height: 1;
  }
  .brand__subtitle {
    margin-top: 8px; font-size: 17px; font-weight: 600;
    letter-spacing: 3px; color: var(--red);
  }
  .dish {
    position: absolute; left: 198px; width: 220px; height: 220px;
    border-radius: 50%; border: 10px solid var(--ring);
  }
  .dish--bread { top: 176px; background: radial-gradient(circle at 45% 45%, #f1ddb4, #c89a5a 70%, #7c5a33); }
  .dish--burger { top: 444px; background: radial-gradient(circle at 50% 55%, #d24a2a, #6a8f2e 45%, #3b2a1c 80%); }
  .dish--drink { top: 712px; background: radial-gradient(circle at 60% 65%, #e86a3a, #8a3a24 45%, #2a2324 80%); }
  .contact {
    position: absolute; left: 94px; right: 0; top: 1000px;
    text-align: center; color: var(--ink);
  }
  .contact__name { font-weight: 700; font-size: 20px; letter-spacing: 1px; margin-bottom: 8px; }
  .contact__line { font-size: 15px; line-height: 1.5; }
</style>
</head>
<body>
  <main class="menu-cover">
    <aside class="side-band">
      <span class="side-band__tagline">Café • Bar • Restaurant</span>
    </aside>

    <header class="brand">
      <div class="brand__name">TOMELLO</div>
      <div class="brand__subtitle">SPEISEKARTE</div>
    </header>

    <div class="dish dish--bread" role="img" aria-label="Foto: Brotkorb mit frischem Gebäck"></div>
    <div class="dish dish--burger" role="img" aria-label="Foto: Burger mit Salat und Tomate"></div>
    <div class="dish dish--drink" role="img" aria-label="Foto: Cocktail an der Bar"></div>

    <footer class="contact">
      <div class="contact__name">Tomello Kassel</div>
      <div class="contact__line">Lindenstraße 12</div>
      <div class="contact__line">34117 · Kassel</div>
      <div class="contact__line">Tel.: 0561 - 48217</div>
    </footer>
  </main>
</body>
</html>
```